Folded A4 flyer for design&construction company

Folded A4 flyer needed. Keywords: elegant, stylish
our website www.corvimo.ae

Industry/Entity Type

Construction

```html
<!DOCTYPE html>
<html lang="en">
<head>
<meta charset="utf-8">
<title>Corvimo – Folded Flyer</title>
<link href="https://fonts.googleapis.com/css2?family=Open+Sans:wght@400;600&family=Ubuntu:wght@400;500;700&family=Dancing+Script:wght@600&family=Arimo:wght@400;700&display=swap" rel="stylesheet">
<style>
  :root{
    --gold:#a37c2c;
    --gold-bright:#c9a23a;
    --quote-orange:#e8a020;
    --ink:#231f20;
    --cream:#f5ede2;
    --cream-light:#fbf8f3;
    --page:#ffffff;
    --white:#ffffff;
  }
  *{margin:0;padding:0;box-sizing:border-box}
  html,body{width:1200px;height:1200px;overflow:hidden;background:var(--page)}
  .canvas{position:relative;width:1200px;height:1200px}
  .side-label{position:absolute;top:146px;width:200px;text-align:center;
    font-family:"Arimo",Arial,sans-serif;font-size:40px;color:#000}
  .side-label.front{left:220px}
  .side-label.back{left:776px}

  .panel{position:absolute;top:233px;height:725px;overflow:hidden}
  .panel.front{left:36px;width:561px;
    background:radial-gradient(ellipse at 50% 30%,var(--cream-light),var(--cream) 90%)}
  .panel.back{left:597px;width:565px;
    background:radial-gradient(ellipse at 50% 35%,var(--cream-light),var(--cream) 95%)}

  .top-band{position:absolute;left:36px;top:222px;width:1126px;height:14px}

  .ornament{position:absolute;border-radius:40% 40% 8px 8px;
    background:linear-gradient(180deg,#e6cf8a,var(--gold-bright) 60%,#d9bc68)}
  .rule{position:absolute;height:3px;background:var(--gold-bright)}

  .brand{position:absolute;left:0;width:100%;text-align:center;
    font-family:"Open Sans",sans-serif;font-weight:400;color:var(--ink);line-height:1}
  .tagline{position:absolute;left:0;width:100%;text-align:center;
    font-family:"Dancing Script",cursive;color:var(--gold);line-height:1}

  /* front */
  .front .ornament{left:132px;top:26px;width:296px;height:120px}
  .front .rule{left:100px;top:150px;width:362px}
  .front .brand{top:160px;font-size:104px;letter-spacing:-2px}
  .front .tagline{top:265px;font-size:32px}
  .interior-photo{position:absolute;left:0;top:280px;width:561px;height:367px;
    background:linear-gradient(180deg,rgba(245,237,226,0) 0%,#dcdad6 22%,#c9cdd0 50%,#a9b6bf 72%,#b7b4ad 100%)}
  .quote-bar{position:absolute;left:0;top:647px;width:561px;height:54px;background:var(--ink);
    color:var(--white);font-family:"Ubuntu",sans-serif;font-weight:500;font-size:22px;
    display:flex;align-items:center;justify-content:center}
  .front .bottom-band{position:absolute;left:0;top:701px;width:561px;height:24px;background:var(--gold)}

  /* back */
  .back .ornament{left:163px;top:23px;width:240px;height:80px}
  .back .rule{left:163px;top:106px;width:240px;height:2px}
  .back .brand{top:116px;font-size:62px;letter-spacing:-1px}
  .back .tagline{top:183px;font-size:20px}
  .about{position:absolute;left:35px;top:215px;width:495px;text-align:center;
    font-family:"Arimo",Arial,sans-serif;font-size:14px;line-height:22.4px;color:#111}
  .divider{position:absolute;left:235px;top:357px;width:94px;height:32px}
  .quote-box{position:absolute;left:97px;top:397px;width:374px;height:133px;border-radius:9px;
    background:var(--ink);text-align:center;font-family:"Arimo",Arial,sans-serif;color:var(--white)}
  .quote-box .cta{margin-top:14px;font-weight:700;font-size:22.5px;color:var(--quote-orange)}
  .quote-box .line{font-size:18.5px;line-height:27px}
  .quote-box .email{color:var(--quote-orange)}
  .back .ornament.lower{left:201px;top:533px;width:162px;height:66px}
  .website{position:absolute;left:0;top:613px;width:100%;text-align:center;
    font-family:"Ubuntu",sans-serif;font-weight:500;font-size:22px;color:var(--ink)}
  .address-bar{position:absolute;left:0;top:647px;width:565px;height:54px;background:var(--gold);
    color:var(--white);font-family:"Ubuntu",sans-serif;font-weight:500;font-size:15.5px;
    display:flex;align-items:center;justify-content:center}
  .back .bottom-band{position:absolute;left:0;top:701px;width:565px;height:24px;background:var(--ink)}
</style>
</head>
<body>
<div class="canvas">
  <div class="side-label front">Front</div>
  <div class="side-label back">Back</div>

  <section class="panel front">
    <div class="ornament" role="img" aria-label="Gold filigree crown ornament"></div>
    <div class="rule"></div>
    <div class="brand">CORVIMO</div>
    <div class="tagline">design &amp; construction</div>
    <div class="interior-photo" role="img" aria-label="Photo of a bright modern living room with white sofas, a fireplace and sea view windows"></div>
    <div class="quote-bar">Quality is not an act, it is a habit – Elian Marsh</div>
    <div class="bottom-band"></div>
  </section>

  <section class="panel back">
    <div class="ornament" role="img" aria-label="Gold filigree crown ornament"></div>
    <div class="rule"></div>
    <div class="brand">CORVIMO</div>
    <div class="tagline">design &amp; construction</div>
    <p class="about">We believe in quality beginnings and flawless finishes. We are a team of creative designers and constructors with years of experience and expertise in providing complete interior design and construction services. Our unique designing prowess is complemented by our unflinching commitment to quality construction. Our team specializes in classic and contemporary high quality construction in Dubai for commercial and residential projects.</p>
    <div class="ornament divider" role="img" aria-label="Small gold filigree divider ornament"></div>
    <div class="quote-box">
      <div class="cta">GET A FREE QUOTE TODAY!</div>
      <div class="line">800 – 2678</div>
      <div class="line">or</div>
      <div class="line email">contact@corvimo.ae</div>
    </div>
    <div class="ornament lower" role="img" aria-label="Gold filigree ornament"></div>
    <div class="website">www.corvimo.ae</div>
    <div class="address-bar">Corvimo LLC, Harbor Point Tower, Office 1208, Marina District, Dubai</div>
    <div class="bottom-band"></div>
  </section>

  <svg class="top-band" viewBox="0 0 1126 14" preserveAspectRatio="none" aria-hidden="true">
    <polygon fill="#a37c2c" points="0,0 1126,0 1126,12 1072,12 1061,5 1050,12 514,12 503,5 492,12 0,12"/>
    <polygon fill="#fbf8f3" points="492,12 503,5 514,12 514,14 492,14"/>
    <polygon fill="#fbf8f3" points="1050,12 1061,5 1072,12 1072,14 1050,14"/>
  </svg>
</div>
</body>
</html>
```